24 hour coin operated Pulse Harbor Workout Center Grand opening.

We are the first of our kind on the planet. I have invented and opened three 24 hour coin operated cardio centers. It's a gym with no weights and no classes. It only has cardio equipment. Imagine a laundromat or a video game arcade, only the machines are treadmills, cross trainers, stair steppers, bikes, etc. my sales person is a coin changer. I have no employees that work in the gym. It's fully automated. I am opening my fourth location and would like to announce its opening, while offering a special pre sale pricing for my tokens. The pre sale pricing is only good until about a week after I open and then the tokens will be regular price. The price is buy 40 tokens get 10 free. My opening day is expected to be Septmebr 14th, so bonus offer ends on the 22nd of Septemebr. I am hoping for a unique design to go along with our unique fitness style.

Target Market(s)

Men and Women from the ages of 14 to 65. all ages really.

Industry/Entity Type

Fitness

Font styles to use
Sans Serif

Colors
fbed22
000000

Requirements
Must have
• Our name and logo P Harbor Workout
• Our FB access name FB:PULSEHARBORWORKOUT
• Must say 24 hours
• Must say worlds first coin operated cardio center.
• Must say grand opening special offer ends Septemebr 22nd
• Phone number: 0958467291
• Must have our address and map:
• No.47, Minsheng Rd., Anping Dist., Tainan City 708 (see attached men for map)
Nice to have
• Website: pulseharborworkout-example.com
Should not have
• Please don't worry about the Chinese characters If I haven't asked you to add them. Sorry, this is to save time for those who haven't been selected.

```html
<!DOCTYPE html>
<html lang="en">
<head>
<meta charset="utf-8">
<title>Pulse Harbor Workout Center – Grand Opening</title>
<link rel="stylesheet" href="https://fonts.googleapis.com/css2?family=Alfa+Slab+One&family=Montserrat:wght@400;600;700;800&display=swap">
<style>
  :root {
    --yellow: #fbed22;
    --black: #000000;
    --ink: #111111;
    --red: #e5202a;
    --orange: #f7a21b;
    --white: #ffffff;
    --rule-grey: #8a8a8a;
    --slab: "Alfa Slab One", serif;
    --sans: "Montserrat", sans-serif;
  }
  * { box-sizing: border-box; margin: 0; padding: 0; }
  html, body { width: 1200px; height: 898px; overflow: hidden; background: var(--black); }
  .poster { position: relative; width: 1200px; height: 898px; overflow: hidden; background: var(--yellow); font-family: var(--sans); }

  .dark-panel { position: absolute; inset: 0; }
  .hero-photo {
    position: absolute; left: 150px; top: 0; width: 470px; height: 898px;
    background: linear-gradient(180deg, #e0b49e 0%, #c7826e 30%, #3a3030 62%, #3c3c3c 100%);
    clip-path: polygon(32% 0, 66% 0, 74% 30%, 100% 55%, 100% 100%, 8% 100%, 14% 55%, 24% 30%);
  }

  .brand { position: absolute; left: 38px; top: 70px; display: flex; align-items: center; gap: 12px; }
  .brand-dot { width: 46px; height: 46px; border-radius: 50%; background: var(--black); }
  .brand-name { font-weight: 800; font-size: 20px; color: var(--black); line-height: 1.15; width: 160px; }

  .headline { position: absolute; left: 680px; top: 30px; width: 480px; text-align: center; }
  .headline-title {
    font-family: var(--slab); font-size: 82px; line-height: 0.92; letter-spacing: 1px;
    background: linear-gradient(180deg, var(--orange) 0%, var(--red) 55%, #b3131a 100%);
    -webkit-background-clip: text; background-clip: text; color: transparent;
  }
  .rule { height: 2px; background: var(--rule-grey); margin: 14px 30px 8px; }
  .location { font-family: var(--slab); font-size: 31px; color: var(--yellow); letter-spacing: 0.5px; }
  .location .star { font-size: 18px; vertical-align: middle; margin: 0 8px; }
  .tagline { font-weight: 700; font-size: 17px; color: var(--white); margin-top: 4px; white-space: nowrap; }

  .offer-circle {
    position: absolute; left: 608px; top: 330px; width: 340px; height: 340px; border-radius: 50%;
    background: var(--yellow); color: var(--ink); text-align: center; padding: 34px 36px 0;
  }
  .offer-stars { color: var(--red); font-size: 12px; letter-spacing: 2px; }
  .offer-buy { font-family: var(--slab); font-size: 48px; line-height: 1; }
  .offer-deal { display: flex; justify-content: center; align-items: center; gap: 6px; margin-top: 2px; }
  .big-red { font-family: var(--slab); font-size: 42px; color: var(--red); line-height: 1; }
  .small-stack { font-size: 14px; font-weight: 600; line-height: 1.05; text-align: left; }
  .free { font-size: 15px; font-weight: 600; color: var(--red); }
  .circle-rule { height: 2px; background: var(--ink); margin: 8px 0; }
  .opening { display: flex; justify-content: center; align-items: flex-end; gap: 6px; }
  .opening-words { text-align: left; }
  .opening-day { font-size: 18px; font-weight: 400; line-height: 1.1; }
  .opening-month { font-family: var(--slab); font-size: 25px; line-height: 1; }
  .opening-date { font-family: var(--slab); font-size: 54px; line-height: 0.9; }
  .opening-date sup { font-size: 22px; vertical-align: top; }
  .presale { margin-top: 10px; color: var(--red); }
  .presale-title { font-family: var(--slab); font-size: 16px; }
  .presale-end { display: flex; justify-content: center; align-items: center; gap: 6px; }
  .presale-num { font-family: var(--slab); font-size: 32px; line-height: 1; }
  .presale-text { font-size: 12px; text-align: left; line-height: 1.1; }
  .presale-text b { font-family: var(--slab); font-weight: 400; font-size: 16px; }

  .hours-banner {
    position: absolute; left: 640px; top: 648px; width: 278px; height: 60px;
    background: var(--red); color: var(--white); font-family: var(--slab); font-size: 38px;
    display: flex; align-items: center; justify-content: center; gap: 10px;
    transform: rotate(-2deg);
  }
  .hours-banner .star { color: var(--yellow); font-size: 14px; }

  .presale-note { position: absolute; left: 958px; top: 342px; color: var(--white); font-size: 20px; font-weight: 400; line-height: 1.15; }
  .map {
    position: absolute; left: 968px; top: 490px; width: 178px; height: 168px;
    background: linear-gradient(135deg, #cfc7b8, #b7ae9d); border: 4px solid var(--red);
  }

  .contact { position: absolute; left: 668px; top: 728px; width: 505px; }
  .address { color: var(--yellow); font-size: 14px; font-weight: 400; text-align: center; white-space: nowrap; }
  .contact-row { display: flex; align-items: center; gap: 9px; margin-top: 12px; white-space: nowrap; }
  .phone { font-family: var(--slab); font-size: 32px; color: var(--yellow); line-height: 1; }
  .web-stack { display: flex; flex-direction: column; gap: 3px; }
  .website, .social { color: var(--yellow); font-size: 13px; font-weight: 600; line-height: 1.1; }
  .icon { flex: none; }
</style>
</head>
<body>
<main class="poster">
  <svg class="dark-panel" width="1200" height="898" viewBox="0 0 1200 898" aria-hidden="true">
    <polygon points="655,0 1200,0 1200,898 560,898 540,300" fill="#000"/>
  </svg>

  <div class="hero-photo" role="img" aria-label="Smiling woman in workout clothes riding a spin bike with a red ribbon"></div>

  <div class="brand">
    <span class="brand-dot"></span>
    <span class="brand-name">P Harbor Workout</span>
  </div>

  <header class="headline">
    <h1 class="headline-title">GRAND<br>OPENING</h1>
    <div class="rule"></div>
    <p class="location"><span class="star">★</span>FOURTH LOCATION<span class="star">★</span></p>
    <div class="rule"></div>
    <p class="tagline">WORLD'S FIRST COIN OPERATED CARDIO CENTER</p>
  </header>

  <section class="offer-circle">
    <div class="offer-stars">★ ★ ★</div>
    <div class="offer-buy">BUY</div>
    <div class="offer-deal">
      <span class="big-red">40</span>
      <span class="small-stack">TOKENS<br>AND GET</span>
      <span class="big-red">10</span>
      <span class="free">FREE</span>
    </div>
    <div class="circle-rule"></div>
    <div class="opening">
      <div class="opening-words">
        <div class="opening-day">OPENING DAY</div>
        <div class="opening-month">SEPTEMBER</div>
      </div>
      <div class="opening-date">14<sup>TH</sup></div>
    </div>
    <div class="presale">
      <div class="presale-title">SPECIAL PRE SALE PRICING</div>
      <div class="presale-end">
        <span class="presale-num">22</span>
        <span class="presale-text">OFFER ENDS ON THE<br><b>ND OF SEPTEMEBR</b></span>
      </div>
    </div>
  </section>

  <div class="hours-banner"><span class="star">★</span>24 HOURS<span class="star">★</span></div>

  <p class="presale-note">SPECIAL PRE<br>SALE PRICING<br>FOR TOKENS<br>UNTIL<br>NEXT WEEK</p>

  <div class="map" role="img" aria-label="Street map showing the location of the new center"></div>

  <footer class="contact">
    <p class="address">No.47, Minsheng Rd., Anping Dist., Tainan City 708</p>
    <div class="contact-row">
      <svg class="icon" width="16" height="28" viewBox="0 0 16 28" aria-hidden="true">
        <rect x="1.5" y="1.5" width="13" height="25" rx="2.5" fill="none" stroke="#fff" stroke-width="2.5"/>
        <circle cx="8" cy="22" r="1.6" fill="#fff"/>
      </svg>
      <span class="phone">0958467291</span>
      <svg class="icon" width="16" height="22" viewBox="0 0 16 22" aria-hidden="true">
        <path d="M8 1a6.5 6.5 0 0 0-6.5 6.5C1.5 12.5 8 20 8 20s6.5-7.5 6.5-12.5A6.5 6.5 0 0 0 8 1z" fill="none" stroke="#fff" stroke-width="2"/>
        <circle cx="8" cy="7.5" r="2.2" fill="#fff"/>
      </svg>
      <div class="web-stack">
        <span class="website">pulseharborworkout-example.com</span>
        <span class="social">FB:PULSEHARBORWORKOUT</span>
      </div>
    </div>
  </footer>
</main>
</body>
</html>
```